Instagram background for quotes

We need a 1080x1080 background for instagram. I use the Phonto app to put text over the image.

We create motivating and inspiring messages for our followers on IG.

Our brands message is, "Mediocre thinking leads to mediocre results. Get Mission - Get Motivated - Get Moving
https://www.example-social.test/steel_resolve_co/

We would like to move away from the rustic look and have a gloss black background with the goal of using text that is cleaner to match the SR in the logo.

I see the design remaining fairly close to what it is now with the logo at the top. I like the quotes on this brand here, https://www.example-social.test/talkwithtycoons/?hl=en. I see this being built into our new background with the quotations being aggressive to match the wings in our logo.

Here is another brand we like - https://www.example-social.test/boomboomdrive/

I've attached the files I was given by the logo designer who has disappeared. I am hoping what is there will suffice.

Target Market(s)

24-34 year old males

Industry/Entity Type

Quotes

Colors
000000
ffffff

Requirements
Must have
• Provided Logo without text
Nice to have
• Aggressive looking quotes to match wings
• Watermark logo in background

```html
<!DOCTYPE html>
<html lang="en">
<head>
<meta charset="UTF-8">
<title>Steel Resolve Quote Post</title>
<link href="https://fonts.googleapis.com/css2?family=Quicksand:wght@400;700&display=swap" rel="stylesheet">
<style>
  :root {
    --ink-white: #ffffff;
    --gloss-black: #000000;
    --gloss-soft: #141414;
    --gloss-sheen: rgba(255, 255, 255, 0.10);
    --gloss-edge: rgba(255, 255, 255, 0.04);
  }
  html, body {
    margin: 0;
    padding: 0;
    width: 1200px;
    height: 1200px;
    overflow: hidden;
    background: var(--gloss-black);
  }
  .post {
    position: relative;
    width: 1200px;
    height: 1200px;
    overflow: hidden;
    font-family: "Quicksand", sans-serif;
    color: var(--ink-white);
  }
  .post__backdrop {
    position: absolute;
    inset: 0;
    background:
      linear-gradient(125deg, transparent 0%, var(--gloss-sheen) 32%, transparent 48%),
      linear-gradient(125deg, transparent 55%, var(--gloss-edge) 68%, transparent 80%),
      radial-gradient(ellipse 70% 50% at 50% 35%, var(--gloss-soft), transparent 75%),
      linear-gradient(180deg, #0a0a0a 0%, var(--gloss-black) 100%);
  }
  .post__frame {
    position: absolute;
    inset: 0;
  }
  .post__brand-mark {
    position: absolute;
    top: 52px;
    left: 0;
    width: 100%;
    text-align: center;
    font-weight: 700;
    font-size: 76px;
    letter-spacing: 8px;
    line-height: 80px;
  }
  .post__quote {
    position: absolute;
    top: 386px;
    left: 0;
    width: 100%;
    margin: 0;
    text-align: center;
    font-weight: 400;
    font-size: 78px;
    line-height: 104px;
    letter-spacing: 1px;
  }
  .post__wordmark {
    position: absolute;
    top: 1062px;
    left: 0;
    width: 100%;
    text-align: center;
    font-weight: 700;
    line-height: 1;
  }
  .post__wordmark-top {
    display: block;
    font-size: 50px;
    letter-spacing: 5px;
  }
  .post__wordmark-bottom {
    display: block;
    margin-top: 8px;
    font-size: 26px;
    letter-spacing: 18px;
    padding-left: 18px;
  }
</style>
</head>
<body>
  <main class="post">
    <div class="post__backdrop" role="img" aria-label="Gloss black background behind the quote"></div>

    <svg class="post__frame" width="1200" height="1200" viewBox="0 0 1200 1200" aria-hidden="true">
      <g fill="none" stroke="#ffffff" stroke-width="4">
        <polyline points="483,78 76,78 76,1122 438,1122"/>
        <polyline points="716,78 1123,78 1123,1122 756,1122"/>
      </g>
    </svg>

    <div class="post__brand-mark">SR</div>

    <p class="post__quote">You're not a failure<br>until you start to<br>blame and make<br>excuses.</p>

    <div class="post__wordmark">
      <span class="post__wordmark-top">STEEL</span>
      <span class="post__wordmark-bottom">RESOLVE</span>
    </div>
  </main>
</body>
</html>
```